A 500th Reformation Anniversary book

I am in need of a front and back cover design.
Front Cover:
The title is "CARRY ME HOME -Konrad Velder". It is an autobiography written as a biography. Velder refers to this book's title in the respect that the book should be thrown into a bonfire and destroyed. Since this is a major part of the climax to the book, and since Velder refers to the title and the cover photo, some type of fire photo is requested. In my working stage, I used a photograph that I had taken on our property.
Back Cover:
I would like a continuation in color from the front. The back will have the typical ISBN, etc. but also a short description of the book and two endorsements.
The final cover will need to be available for the following:
This book will have three formats. The book will be:
8.5" x 11" spiral bound - no spine
8.5" x 5.5" perfect bound
ebook
I do not have the exact spine width, but the page count for the perfect bound is 190.
I have confirmed that I will receive final copy that I can work with. I will need to add "School Edition" to the cover for the Spiral Bound.
I believe that's everything you need!
Thank you!
K.T.Dorran

Target Market(s)

Middle School-Aged Children through Adults

Font styles to use
Sans Serif

Requirements
Must have
• See Project description plus...
• Title should be written such that it is clear that the 'Konrad Velder' part of it is simply a byline to the words CARRY ME HOME.

```html
<!DOCTYPE html>
<html lang="en">
<head>
<meta charset="utf-8">
<title>Carry Me Home – Back Cover</title>
<link href="https://fonts.googleapis.com/css2?family=Oswald:wght@500;600&family=Questrial&display=swap" rel="stylesheet">
<style>
  :root {
    --bg-slate: #2a2f3a;
    --flame-gold: #fbb731;
    --flame-orange: #f08a24;
    --flame-red: #b0281e;
    --text-light: #ffffff;
    --isbn-white: #ffffff;
  }
  * { margin: 0; padding: 0; box-sizing: border-box; }
  html, body { width: 934px; height: 1200px; overflow: hidden; }
  body { background: var(--bg-slate); }
  .back-cover {
    position: relative;
    width: 934px;
    height: 1200px;
    background: var(--bg-slate);
    color: var(--text-light);
    font-family: "Questrial", "Century Gothic", sans-serif;
    overflow: hidden;
  }
  .title {
    position: absolute;
    top: 36px;
    left: 0;
    width: 100%;
    text-align: center;
    font-family: "Oswald", "Arial Narrow", sans-serif;
    font-weight: 600;
    font-size: 116px;
    line-height: 1.2;
    letter-spacing: 1px;
    background: linear-gradient(180deg, var(--flame-red) 0%, var(--flame-orange) 35%, var(--flame-gold) 60%, var(--flame-orange) 100%);
    -webkit-background-clip: text;
    background-clip: text;
    color: transparent;
  }
  .byline {
    position: absolute;
    top: 190px;
    left: 0;
    width: 100%;
    text-align: center;
    font-family: "Oswald", "Arial Narrow", sans-serif;
    font-weight: 500;
    font-size: 54px;
    line-height: 1.1;
  }
  .invitation {
    position: absolute;
    top: 302px;
    left: 0;
    width: 100%;
    text-align: center;
    font-size: 20px;
  }
  .blurb {
    position: absolute;
    top: 342px;
    left: 140px;
    width: 654px;
    text-align: center;
    font-size: 17.5px;
    line-height: 23.5px;
  }
  .blurb p + p { margin-top: 11px; }
  .endorsements {
    position: absolute;
    top: 596px;
    left: 147px;
    width: 640px;
    font-size: 16.2px;
    line-height: 21.6px;
  }
  .endorsement-quote { text-indent: 53px; }
  .endorsement-source {
    display: flex;
    margin-top: 10px;
    margin-bottom: 11px;
  }
  .source-name { width: 214px; flex-shrink: 0; }
  .footer-band {
    position: absolute;
    left: 0;
    bottom: 0;
    width: 100%;
    height: 123px;
    background: linear-gradient(90deg, var(--flame-gold) 0%, var(--flame-gold) 58%, var(--flame-orange) 75%, var(--flame-red) 100%);
  }
  .isbn-box {
    position: absolute;
    left: 579px;
    top: 1027px;
    width: 214px;
    height: 133px;
    background: var(--isbn-white);
  }
</style>
</head>
<body>
<main class="back-cover">
  <h1 class="title">CARRY ME HOME</h1>
  <p class="byline">- Konrad Velder</p>

  <p class="invitation">“Come on in. Have a seat.”</p>

  <div class="blurb">
    <p>In these pages you will be transported to Konrad Velder’s home. You will sit with him at his kitchen table as he reveals the unexpected twists and turns that took place in his life. His wife will visit with you briefly, but for a reason you might not expect.</p>
    <p>In the end, this book may not be about Velder at all!<br>You decide.</p>
  </div>

  <section class="endorsements">
    <p class="endorsement-quote">“The first-person narrative style of this book will especially appeal to children. The full color original photographs will capture their attention and bring the stories to life. This book makes an excellent classroom textbook but it will easily appeal to the adult reader looking to deepen their understanding about the life of Velder.”</p>
    <div class="endorsement-source">
      <span class="source-name">-Mr. Paul Hartwig,</span>
      <span class="source-role">retired Parochial Grade School Teacher and Principal (NCS)</span>
    </div>
    <p class="endorsement-quote">"I loved the way in which the author wrote the book in the first person. It was as if Konrad Velder himself were telling me his story and explaining the struggle which engulfed him and the Church during the time of the Reformation. The story telling and vocabulary make this an excellent source for teaching children and adults about the life of Velder. The wonderful color photography places you in Germany. My wish is to share a copy of this fascinating book with every member in my congregations."</p>
    <div class="endorsement-source">
      <span class="source-name">-Rev. Samuel Krause,</span>
      <span class="source-role">Pastor at Grace and Hope Ev. Churches, northern Ohio, NCS</span>
    </div>
  </section>

  <div class="footer-band"></div>
  <div class="isbn-box" aria-label="ISBN block area"></div>
</main>
</body>
</html>
```